Flyer for an online formula one racing league

Hello.

I am looking for the perfect one page facebook/instagram style flyer for an online formula one racing league. The racing league is called 'VOLTA RACING LEAGUE'.

Information that MUST be on the new flyer is already on the old flyer I have uploaded here. In addition to including: The Volta racing league VOLTA I have uploaded AND the text: 'Very popular, clean and competitive racing league, running for its 4th season. Why not join with a friend? Race times, Mondays, Tuesdays and Wednesdays each at 8pm UK TIME Message below for any questions. (Spacing of information is not important, however all the information in regards to the racing I have just mentioned MUST BE on the flyer, this includes info from old pic, logo and the other info I just mentioned).

It would be beneficial to have lots of dark blue on the flyer and the new flyer to be a lot different to the original flyer I uploaded, but this is not essential.

I apologise if I did not explain very well, any questions, please message me.

The best flyer should look the most attractive to someone that might be interested in joining an online formula one racing league.

I used this website before to create the perfect logo for my Sunday League team last year, and I was very impressed. I look forward to seeing your submissions.

Target Market(s)

No specific target, more something that may attract someone into joining a formula one online racing league

Industry/Entity Type

e sports/formula one

Colors
0054AA
0677BA
7BADD7
CADEEF
E8F1F8

Requirements
Must have
• Read product description please
Should not have
• Ignoring product description!

```html
<!DOCTYPE html>
<html lang="en">
<head>
<meta charset="utf-8">
<title>Volta Racing League – Flyers</title>
<link rel="stylesheet" href="https://fonts.googleapis.com/css2?family=Archivo:ital,wdth,wght@1,125,900&family=Barlow+Condensed:ital,wght@1,900&family=Poppins:ital,wght@0,400;0,600;0,700;1,300&display=swap">
<style>
  :root {
    --page-blue: #06288f;
    --card-navy: #0c1f6e;
    --card-deep: #0a1550;
    --ink-white: #ffffff;
    --ink-soft: #dfe6ff;
    --accent-yellow: #f7c600;
    --accent-pink: #ef2d83;
    --stripe-blue: #1f3bff;
    --badge-dark: #0b1236;
    --check-light: #d9d9d9;
    --check-dark: #7b7b7b;
  }
  * { margin: 0; padding: 0; box-sizing: border-box; }
  html, body {
    width: 1200px; height: 1166px; overflow: hidden;
    background: var(--page-blue);
    font-family: "Poppins", sans-serif;
    color: var(--ink-white);
  }
  .flyer {
    position: absolute; left: 111px; width: 977px; height: 512px;
    overflow: hidden;
    box-shadow: 0 14px 28px rgba(0, 0, 20, 0.45);
  }
  .flyer--classic { top: 54px; background: var(--card-navy); }
  .flyer--photo { top: 609px; background: var(--card-deep); }

  .layer { position: absolute; inset: 0; }
  .line {
    position: absolute; left: 0; width: 100%;
    text-align: center; line-height: 1; white-space: nowrap;
    transform: translateY(-50%);
  }
  .badge {
    position: absolute; border-radius: 50%;
    background: var(--badge-dark);
    display: flex; align-items: center; justify-content: center;
    font-weight: 700; font-size: 19px; letter-spacing: 0.5px;
    color: var(--ink-white);
  }
  .schedule { font-weight: 700; font-size: 24px; }
  .season { font-weight: 700; font-size: 30px; color: var(--accent-yellow); }
  .tagline { font-weight: 600; font-size: 28px; }
  .pitch { font-weight: 400; font-size: 19px; color: var(--ink-soft); }
  .divisions { font-weight: 400; font-size: 23px; }
  .divisions strong { font-weight: 700; }
  .invite { font-weight: 700; font-size: 20px; }
  .inquiries { font-weight: 700; color: var(--accent-pink); }

  /* classic flyer */
  .flyer--classic .badge { left: 135px; top: 40px; width: 98px; height: 98px; }
  .classic-title {
    position: absolute; left: 253px; top: 60px;
    font-family: "Barlow Condensed", sans-serif; font-style: italic; font-weight: 900;
    font-size: 74px; line-height: 1; white-space: nowrap;
  }
  .classic-sub {
    position: absolute; left: 133px; top: 162px; transform: translateY(-50%);
    font-style: italic; font-weight: 300; font-size: 29px; line-height: 1;
  }
  .speed-stripe { position: absolute; left: 501px; right: 0; top: 153px; height: 18px; }
  .speed-stripe::before, .speed-stripe::after {
    content: ""; position: absolute; left: 0; right: 0; height: 50%;
  }
  .speed-stripe::before { top: 0; background: var(--accent-pink); }
  .speed-stripe::after { bottom: 0; background: var(--stripe-blue); }
  .flyer--classic .inquiries { font-size: 20px; }

  /* photo flyer */
  .flyer--photo .scene {
    background:
      radial-gradient(ellipse 14% 22% at 15% 19%, rgba(60,110,220,0.5), transparent 70%),
      linear-gradient(160deg, rgba(40,170,220,0.3) 0%, transparent 22%),
      linear-gradient(200deg, rgba(200,40,80,0.18) 0%, transparent 30%),
      linear-gradient(335deg, rgba(40,170,220,0.3) 0%, transparent 18%),
      radial-gradient(ellipse 40% 45% at 85% 40%, #1f2a7a, transparent 75%),
      linear-gradient(180deg, #1a2a86 0%, #101a66 50%, #080f45 100%);
  }
  .flyer--photo .badge { left: 440px; top: 37px; width: 96px; height: 96px; }
  .photo-title {
    font-family: "Archivo", sans-serif; font-style: italic; font-weight: 900;
    font-stretch: 125%; font-size: 47px;
  }
  .photo-sub { font-style: italic; font-weight: 300; font-size: 22px; }
  .flyer--photo .pitch { font-size: 18px; }
  .flyer--photo .invite { font-size: 19px; }
  .flyer--photo .inquiries { font-size: 17px; }
</style>
</head>
<body>

<section class="flyer flyer--classic">
  <svg class="layer" width="977" height="512" viewBox="0 0 977 512" role="img" aria-label="Chequered flag banners across the corners">
    <defs>
      <linearGradient id="flagTone" x1="0" y1="0" x2="1" y2="1">
        <stop offset="0" stop-color="var(--check-light)"/>
        <stop offset="1" stop-color="var(--check-dark)"/>
      </linearGradient>
    </defs>
    <polygon points="0,0 181,0 0,122" fill="url(#flagTone)"/>
    <polygon points="702,512 792,512 977,385 977,324" fill="url(#flagTone)"/>
  </svg>
  <div class="badge">VOLTA</div>
  <h1 class="classic-title">VOLTA RACING LEAGUE</h1>
  <p class="classic-sub">Running for its 4th season</p>
  <div class="speed-stripe"></div>
  <p class="line schedule" style="top:226px">Mondays, Tuesdays and Wednesdays each at 8pm UK TIME</p>
  <p class="line season" style="top:280px">New season just starting!!!</p>
  <p class="line tagline" style="top:317px">Clean Online Racing League</p>
  <p class="line pitch" style="top:352px">Very popular, clean and competitive racing league</p>
  <p class="line divisions" style="top:394px"><strong>3 divisions</strong> currently and looking to keep growing!</p>
  <p class="line invite" style="top:431px">Why not join with a friend?</p>
  <p class="line inquiries" style="top:470px">Feel free to message us for any inquiries!</p>
</section>

<section class="flyer flyer--photo">
  <div class="layer scene" role="img" aria-label="Race car speeding along a night track with light streaks and a speedometer"></div>
  <div class="badge">VOLTA</div>
  <h1 class="line photo-title" style="top:172px">VOLTA RACING LEAGUE</h1>
  <p class="line photo-sub" style="top:210px">Running for its 4th season</p>
  <p class="line pitch" style="top:242px">Very popular, clean and competitive racing league</p>
  <p class="line schedule" style="top:284px">Mondays, Tuesdays and Wednesdays each at 8pm UK TIME</p>
  <p class="line season" style="top:330px">New season just starting!!!</p>
  <p class="line tagline" style="top:366px">Clean Online Racing League</p>
  <p class="line divisions" style="top:408px">3 divisions currently and looking to keep growing!</p>
  <p class="line invite" style="top:443px">Why not join with a friend?</p>
  <p class="line inquiries" style="top:478px">Feel free to message us for any inquiries!</p>
</section>

</body>
</html>
```